Brochure design for a Driftly Video Booth!

We are after a brochure for a Driftly Video Booth product being launched very soon. Attached are the logo, photos and all required information to be included in this brochure.

I have also attached a number of "inspiration" designs to show you the style we are after.

The colours should be black, white and a warm yellow (see attachment).

The brochure is for online use only, so does not need to constrain to typical printing specs. A square or rectangular booklet would be preferable.

Target Market(s)

Couples getting married between 20 - 35.

Industry/Entity Type

Printing

Font styles to use
Serif
Sans Serif

Colors
fece3e
000000
ffffff

Requirements
Must have
• at least 4 pages, a 'typography' design feel, good use of space. The colours should be black, white and a warm yellow (see attachment). Feel free to use whatever layout you think would work best.
Should not have
• Clutter.

```html
<!DOCTYPE html>
<html lang="en">
<head>
<meta charset="utf-8">
<title>Driftly Package</title>
<link rel="stylesheet" href="https://fonts.googleapis.com/css2?family=Antonio:wght@400;700&family=Inter:wght@500;800&display=swap">
<style>
  :root {
    --black: #000000;
    --white: #ffffff;
    --gold: #fed20c;
    --bright-yellow: #fff200;
    --shadow-grey: #808080;
  }
  html, body {
    margin: 0;
    padding: 0;
    width: 1200px;
    height: 776px;
    overflow: hidden;
    background: var(--white);
  }
  .canvas {
    position: relative;
    width: 1200px;
    height: 776px;
    overflow: hidden;
    background: var(--white);
    font-family: "Inter", Arial, sans-serif;
  }
  .drop-shadow {
    position: absolute;
    left: 27px; top: 708px;
    width: 1122px; height: 32px;
    background: var(--shadow-grey);
  }
  .title-panel {
    position: absolute;
    left: 13px; top: 30px;
    width: 717px; height: 678px;
    background: var(--black);
  }
  .divider-bar {
    position: absolute;
    left: 731px; top: 0;
    width: 47px; height: 776px;
    background: var(--bright-yellow);
  }
  .features-panel {
    position: absolute;
    left: 779px; top: 30px;
    width: 409px; height: 665px;
    background: var(--black);
  }
  .contact-strip {
    position: absolute;
    left: 779px; top: 695px;
    width: 421px; height: 13px;
    background: var(--bright-yellow);
    color: var(--black);
    font-size: 13px;
    font-weight: 500;
    line-height: 1;
  }
  .contact-label { position: absolute; left: 28px; top: 2px; }
  .contact-email { position: absolute; right: 28px; top: 0; }

  .title-word {
    position: absolute;
    margin: 0;
    color: var(--white);
    font-weight: 800;
    line-height: 1;
    letter-spacing: -0.035em;
  }
  .title-our { left: 18px; top: 36px; font-size: 122px; }
  .title-package { left: 56px; top: 491px; font-size: 132px; }

  .name-block {
    position: absolute;
    left: 0; top: 199px;
    width: 537px; height: 214px;
    background: var(--gold);
    overflow: hidden;
  }
  .name-block span {
    position: absolute;
    left: 78px; top: 11px;
    font-family: "Antonio", "Arial Narrow", sans-serif;
    font-weight: 400;
    font-size: 168px;
    line-height: 1;
    color: var(--black);
    letter-spacing: -0.01em;
  }

  .price {
    position: absolute;
    right: 488px; top: 38px;
    margin: 0;
    font-family: "Antonio", "Arial Narrow", sans-serif;
    font-weight: 700;
    font-size: 44px;
    line-height: 1;
    color: var(--white);
  }

  .feature {
    position: absolute;
    right: 32px;
    margin: 0;
    width: 380px;
    text-align: right;
    color: var(--white);
    font-size: 14.5px;
    font-weight: 500;
    line-height: 22px;
  }
  .feature-travel { top: 78px; }
  .feature-props { top: 194px; }
  .feature-hours { top: 302px; }
  .feature-footage { top: 388px; }
  .feature-edit { top: 464px; }
  .feature-usb { top: 564px; }
</style>
</head>
<body>
<main class="canvas">
  <div class="drop-shadow"></div>

  <section class="title-panel"></section>
  <h1 class="title-word title-our">Our</h1>
  <div class="name-block"><span>Driftly</span></div>
  <h1 class="title-word title-package">Package</h1>
  <p class="price">$1200</p>

  <div class="divider-bar"></div>

  <section class="features-panel"></section>
  <p class="feature feature-travel">Travel to your wedding, party or event in the<br>Cairns/Port Douglas region</p>
  <p class="feature feature-props">A massive selection of props (Glitter, silly string,<br>confetti, foam blasters, party poppers etc…)</p>
  <p class="feature feature-hours">2 hours of Driftly booth fun</p>
  <p class="feature feature-footage">All footage shot at 200fps in Full HD</p>
  <p class="feature feature-edit">Your video edited and uploaded to a shareable link</p>
  <p class="feature feature-usb">A USB drive of the edited video.</p>

  <div class="contact-strip">
    <span class="contact-label">Email</span>
    <span class="contact-email">info@driftly.com.au</span>
  </div>
</main>
</body>
</html>
```